Stationary for Keeping Steady

we are in the process of creating a more professional image for our company Keeping Steady Paramedical Services. We have recently had a new logo and general brochure designed using artpitchhub and have been impressed by the quality of submissions.

We need:
- Letterhead (A4)
- Business Cards
- With compliments slips
- Email stationary

Letterhead information:
Address - 47 Wattlebrook Drive, Fernhollow Vic 3091
Phone - 1800 462 817
email - enquiries@keepsteady.com.au
Internet - www.keepsteady.com.au
ABN - 82 463 915 207
ACN - 264 871 035

Files need to be able to be edited in Illustrator CS2

Business Cards / with compliments slips / email stationary:
Double sided.
One side to have Name, Mobile number, company phone 1800462817, email, internet address

Files need to be able to be edited in Illustrator CS2 (except email stationary)

Our website is www.keepsteady.com.au for more information. Do not base designs on the website as it will eventually be revised.

Target Market(s)

Australian based businesses, government departments and schools. We specialise in corporate customers rather than public first aid course

Industry/Entity Type

Internet

Requirements
Must have
• Where applicable file to be editable in illustrator CS2 to allow future alterations.

```html
<!DOCTYPE html>
<html lang="en">
<head>
<meta charset="utf-8">
<title>Keeping Steady – Business Card</title>
<link href="https://fonts.googleapis.com/css2?family=Open+Sans:wght@400;600;700&display=swap" rel="stylesheet">
<style>
  :root {
    --backdrop: #1e1e1f;
    --card-white: #ffffff;
    --brand-red: #d6222b;
    --band-red-dark: #a81b22;
    --band-red-light: #e0202a;
    --ink: #1a1a1a;
    --ink-soft: #333333;
  }
  html, body {
    margin: 0;
    padding: 0;
    width: 1027px;
    height: 1200px;
    overflow: hidden;
    background: var(--backdrop);
    font-family: "Open Sans", Arial, sans-serif;
  }
  .stage {
    position: relative;
    width: 1027px;
    height: 1200px;
  }

  /* ---------- Front of card ---------- */
  .card-front {
    position: absolute;
    left: 131px;
    top: 110px;
    width: 760px;
    height: 462px;
    background: var(--card-white);
    overflow: hidden;
  }
  .brand {
    position: absolute;
    display: flex;
    align-items: center;
    gap: 16px;
    color: var(--brand-red);
    font-weight: 700;
  }
  .brand-mark {
    flex: none;
    background: var(--brand-red);
  }
  .brand-name {
    line-height: 1.05;
  }
  .brand-name .line-main { display: block; }
  .brand-name .line-sub { display: block; }

  .card-front .brand { left: 165px; top: 50px; }
  .card-front .brand-mark { width: 54px; height: 54px; }
  .card-front .line-main { font-size: 42px; }
  .card-front .line-sub { font-size: 21px; margin-top: 4px; }

  .holder {
    position: absolute;
    left: 50px;
    top: 230px;
  }
  .holder-name {
    font-size: 28px;
    font-weight: 400;
    color: var(--ink);
    letter-spacing: 0.5px;
    margin: 0;
  }
  .holder-title {
    font-size: 17px;
    color: var(--ink-soft);
    letter-spacing: 1px;
    margin: 2px 0 0;
  }

  .contact {
    position: absolute;
    left: 381px;
    top: 232px;
    font-size: 18px;
    color: var(--ink);
    letter-spacing: 0.6px;
    line-height: 29px;
  }
  .contact-address { text-transform: uppercase; }
  .contact-line {
    display: flex;
    align-items: center;
    gap: 9px;
    height: 31px;
  }
  .contact-line svg { width: 20px; height: 20px; fill: var(--brand-red); flex: none; }
  .contact-email { color: var(--brand-red); font-weight: 700; }

  .web-band {
    position: absolute;
    left: 0;
    bottom: 0;
    width: 100%;
    height: 57px;
    background: linear-gradient(90deg, var(--band-red-dark), var(--band-red-light));
    color: var(--card-white);
    font-weight: 700;
    font-size: 20px;
    letter-spacing: 15px;
    display: flex;
    align-items: center;
    justify-content: center;
  }

  /* ---------- Back of card ---------- */
  .card-back {
    position: absolute;
    left: 125px;
    top: 638px;
    width: 770px;
    height: 462px;
    border: 1px solid #f2f2f2;
    background: linear-gradient(100deg, var(--band-red-dark) 0%, #c41f26 50%, var(--band-red-light) 100%);
    overflow: hidden;
  }
  .brand-tab {
    position: absolute;
    left: 0;
    top: 151px;
    width: 495px;
    height: 116px;
    background: var(--card-white);
    border-radius: 0 58px 58px 0;
  }
  .card-back .brand { left: 68px; top: 24px; }
  .card-back .brand-mark { width: 46px; height: 46px; }
  .card-back .line-main { font-size: 37px; }
  .card-back .line-sub { font-size: 18px; margin-top: 3px; }

  .web-address {
    position: absolute;
    left: 0;
    width: 100%;
    top: 308px;
    text-align: center;
    color: var(--card-white);
    font-size: 35px;
    letter-spacing: 7px;
    padding-right: 30px;
    box-sizing: border-box;
  }
</style>
</head>
<body>
<main class="stage">

  <section class="card-front" aria-label="Business card front">
    <div class="brand">
      <span class="brand-mark"></span>
      <span class="brand-name">
        <span class="line-main">Keeping Steady</span>
        <span class="line-sub">Paramedical Services Pty Ltd</span>
      </span>
    </div>

    <div class="holder">
      <p class="holder-name">Daniel Harrow</p>
      <p class="holder-title">PHARAMEDICAL MANAGER</p>
    </div>

    <div class="contact">
      <div class="contact-address">47 Wattlebrook Drive,<br>Fernhollow Vic 3091</div>
      <div class="contact-line">
        <svg viewBox="0 0 20 20" aria-label="Phone"><path d="M2 8c0-3 4-5 8-5s8 2 8 5l-3 1-1-2c-2-1-6-1-8 0l-1 2zM5 10h10l2 7H3z M10 11.5a2.5 2.5 0 1 0 .01 0z"/></svg>
        <span>1800 462 817</span>
      </div>
      <div class="contact-line">
        <svg viewBox="0 0 20 20" aria-label="Mobile"><path d="M6 1h8a1 1 0 0 1 1 1v16a1 1 0 0 1-1 1H6a1 1 0 0 1-1-1V2a1 1 0 0 1 1-1zm1 2v8h6V3zm0 10v2h2v-2zm4 0v2h2v-2z"/></svg>
        <span>1800 462 817</span>
      </div>
      <div class="contact-line">
        <svg viewBox="0 0 20 20" aria-label="Email"><path d="M1 4h18v12H1zm2 2v.5l7 5 7-5V6l-7 5z"/></svg>
        <span class="contact-email">enquiries@keepsteady.com.au</span>
      </div>
    </div>

    <div class="web-band">www.keepsteady.com.au</div>
  </section>

  <section class="card-back" aria-label="Business card back">
    <div class="brand-tab">
      <div class="brand">
        <span class="brand-mark"></span>
        <span class="brand-name">
          <span class="line-main">Keeping Steady</span>
          <span class="line-sub">Paramedical Services Pty Ltd</span>
        </span>
      </div>
    </div>
    <div class="web-address">www.keepsteady.com.au</div>
  </section>

</main>
</body>
</html>
```